Flyer-Design für syrisch-orthodoxe Kirche in Österreich
Super schnell und auf alle Wünsche bestens reagiert!
Zielgruppe
Wir sind eine Pfarre die gerade dabei ist den ersten Neubau der syrisch-orthodoxen Kirche in Österreich, in welcher die Muttersprache Jesu gesprochen wird, zu errichten.
Ausführliche Informationen über unsere Gemeinde sowie unser Vorhaben findet ihr in den angehängten Dateien.
Aufgabenstellung
Textvorlagen sowie das angedachte Format sind in den Anhängen vorhanden und erläutert.
Aber auch Querdenker sind sehr gerne eingeladen ihre eigenen Ideen zu präsentieren :)
Wir werden versuchen so rasch wie möglich auf die Entwürfe bzw. auch auf Fragen zu reagieren um gemeinsam ein optimales Ergebnis zu erreichen!
EDIT:
Bitte den öffentlichen Kommentar beachten!

```html
<!DOCTYPE html>
<html lang="de">
<head>
<meta charset="utf-8">
<title>Flyer-Entwürfe – Syrisch-orthodoxe Gemeinde</title>
<link href="https://fonts.googleapis.com/css2?family=Open+Sans:wght@400;600;700&family=Arimo&display=swap" rel="stylesheet">
<style>
  :root {
    --board: #cdcdcd;
    --paper: #ffffff;
    --ink: #111111;
    --gold: #d2a735;
    --gold-light: #e6c87a;
    --beige: #f1e5cc;
    --rule: #6d6d6d;
    --hatch: #c4c4c4;
    --sky-top: #a6d8f1;
    --sky-low: #d3ecf6;
    --field-far: #86b43e;
    --field-near: #4f8d1f;
    --art-light: #efefef;
    --art-dark: #bdbdbd;
  }
  * { box-sizing: border-box; margin: 0; padding: 0; }
  html, body { width: 1200px; height: 1200px; overflow: hidden; }
  body {
    background: var(--board);
    font-family: "Open Sans", Arial, sans-serif;
    position: relative;
  }
  .variant-number {
    position: absolute;
    font-family: Arimo, Arial, sans-serif;
    font-size: 32px;
    line-height: 1;
    color: var(--ink);
  }
  .flyer {
    position: absolute;
    width: 456px;
    height: 221px;
    background: var(--paper);
    overflow: hidden;
    box-shadow: 0 4px 14px rgba(0,0,0,0.28);
  }
  .field-photo {
    position: absolute; inset: 0;
    background: linear-gradient(to bottom,
      var(--sky-top) 0%, var(--sky-low) var(--horizon),
      var(--field-far) var(--horizon), var(--field-near) 100%);
  }
  .madonna-art {
    position: absolute;
    background: radial-gradient(ellipse at 50% 40%, var(--art-light) 0%, var(--art-dark) 100%);
    border-radius: 46% 46% 10% 10%;
  }
  .madonna-art.faint { opacity: 0.55; }
  .quote {
    position: absolute;
    font-weight: 600;
    font-size: 12.4px;
    line-height: 17px;
    white-space: nowrap;
    color: var(--ink);
  }
  .quote .line { display: block; padding-left: 3px; }
  .quote .line.first { padding-left: 0; }
  .quote.on-photo { color: #fff; text-shadow: 0 1px 2px rgba(0,0,0,0.55); }
  .quote.on-gold { color: #fff; }
  .quote.in-gold { color: var(--gold); font-size: 13.6px; line-height: 17px; }
  .reference {
    position: absolute;
    font-weight: 700;
    font-size: 8.6px;
    color: var(--ink);
    white-space: nowrap;
  }
  .reference.on-photo { color: #fff; text-shadow: 0 1px 2px rgba(0,0,0,0.55); }
  .reference.on-gold { color: #fff; }
  .reference.in-gold { color: var(--gold); font-weight: 600; }
  .church-header { position: absolute; }
  .church-header .script-line {
    position: absolute;
    height: 8px;
    background: linear-gradient(to right, rgba(17,17,17,0.75), rgba(17,17,17,0.55));
    border-radius: 2px;
  }
  .church-header .mark {
    position: absolute;
    width: 22px; height: 22px;
    border-radius: 50%;
    background: var(--ink);
  }
  .church-header .name {
    position: absolute;
    font-size: 7.4px;
    font-weight: 600;
    color: var(--ink);
    white-space: nowrap;
  }
  .hatch-band {
    position: absolute;
    background: repeating-linear-gradient(135deg, var(--hatch) 0 1px, transparent 1px 3px);
  }
  .divider { position: absolute; height: 1.5px; background: var(--rule); }
  svg.shape { position: absolute; inset: 0; }
</style>
</head>
<body>

<!-- Variante 1 -->
<span class="variant-number" style="left:50px; top:52px;">1</span>
<div class="flyer" style="left:80px; top:66px;">
  <div class="field-photo" style="--horizon:20%;" role="img" aria-label="Foto: grünes Getreidefeld unter blauem Himmel"></div>
  <div class="madonna-art" style="left:32px; top:45px; width:95px; height:123px;" role="img" aria-label="Zeichnung: Ikone der Gottesmutter mit Kind"></div>
  <div class="quote on-photo" style="left:156px; top:79px;">
    <span class="line first">„Ich aber sage dir:</span>
    <span class="line">Du bist Petrus, und auf diesen Felsen werde</span>
    <span class="line">ich meine Kirche bauen, und die Mächte der</span>
    <span class="line">Unterwelt werden sie nicht überwältigen.“</span>
  </div>
  <div class="reference on-photo" style="right:32px; top:156px;">Matthaeus 16:18</div>
</div>

<!-- Variante 2 -->
<span class="variant-number" style="left:52px; top:350px;">2</span>
<div class="flyer" style="left:80px; top:364px;">
  <div class="madonna-art" style="left:24px; top:45px; width:117px; height:152px;" role="img" aria-label="Zeichnung: Ikone der Gottesmutter mit Kind"></div>
  <div class="quote" style="left:153px; top:69px;">
    <span class="line first">„Ich aber sage dir:</span>
    <span class="line">Du bist Petrus, und auf diesen Felsen werde</span>
    <span class="line">ich meine Kirche bauen, und die Mächte der</span>
    <span class="line">Unterwelt werden sie nicht überwältigen.“</span>
  </div>
  <div class="reference" style="right:43px; top:144px;">Matthaeus 16:18</div>
</div>

<!-- Variante 3 -->
<span class="variant-number" style="left:52px; top:648px;">3</span>
<div class="flyer" style="left:80px; top:661px;">
  <div class="field-photo" style="--horizon:36%;" role="img" aria-label="Foto: grünes Feld mit Feldweg und Baum unter blauem Himmel"></div>
  <div class="church-header" style="left:0; top:0;">
    <span class="mark" style="left:58px; top:31px;"></span>
    <span class="script-line" style="left:98px; top:32px; width:257px;" role="img" aria-label="Gemeindename in syrischer Schrift"></span>
    <span class="name" style="left:98px; top:46px;">Syrisch-Orthodoxe Gemeinde St. Ephräm in Graz</span>
  </div>
  <div class="quote on-photo" style="left:98px; top:98px;">
    <span class="line first">„Ich aber sage dir:</span>
    <span class="line">Du bist Petrus, und auf diesen Felsen werde</span>
    <span class="line">ich meine Kirche bauen, und die Mächte der</span>
    <span class="line">Unterwelt werden sie nicht überwältigen.“</span>
  </div>
  <div class="reference on-photo" style="right:99px; top:173px;">Matthaeus 16:18</div>
</div>

<!-- Variante 4 -->
<span class="variant-number" style="left:52px; top:922px;">4</span>
<div class="flyer" style="left:80px; top:935px;">
  <div class="madonna-art" style="left:30px; top:61px; width:79px; height:104px;" role="img" aria-label="Zeichnung: Ikone der Gottesmutter mit Kind"></div>
  <div class="quote in-gold" style="left:131px; top:74px;">
    <span class="line first">„Ich aber sage dir:</span>
    <span class="line">Du bist Petrus, und auf diesen Felsen werde</span>
    <span class="line">ich meine Kirche bauen, und die Mächte der</span>
    <span class="line">Unterwelt werden sie nicht überwältigen.“</span>
  </div>
  <div class="divider" style="left:134px; top:150px; width:211px;"></div>
  <div class="reference in-gold" style="left:352px; top:144px;">Matthaeus 16:18</div>
</div>

<!-- Variante 5 -->
<span class="variant-number" style="left:594px; top:52px;">5</span>
<div class="flyer" style="left:624px; top:66px;">
  <svg class="shape" width="456" height="221" viewBox="0 0 456 221" aria-hidden="true">
    <polygon points="0,208 456,182 456,211 0,211" fill="var(--beige)"/>
    <polygon points="0,210 456,196 456,211 0,211" fill="var(--gold-light)" opacity="0.6"/>
    <rect x="0" y="211" width="456" height="10" fill="var(--gold)"/>
  </svg>
  <div class="madonna-art" style="left:17px; top:24px; width:123px; height:159px;" role="img" aria-label="Zeichnung: Ikone der Gottesmutter mit Kind"></div>
  <div class="quote" style="left:162px; top:43px;">
    <span class="line first">„Ich aber sage dir:</span>
    <span class="line">Du bist Petrus, und auf diesen Felsen werde</span>
    <span class="line">ich meine Kirche bauen, und die Mächte der</span>
    <span class="line">Unterwelt werden sie nicht überwältigen.“</span>
  </div>
  <div class="reference" style="right:23px; top:120px;">Matthaeus 16:18</div>
</div>

<!-- Variante 6 -->
<span class="variant-number" style="left:594px; top:350px;">6</span>
<div class="flyer" style="left:624px; top:364px;">
  <div class="field-photo" style="--horizon:37%;" role="img" aria-label="Foto: weites grünes Feld mit Baum unter Wolkenhimmel"></div>
  <div class="church-header" style="left:0; top:0;">
    <span class="mark" style="left:60px; top:28px;"></span>
    <span class="script-line" style="left:99px; top:29px; width:258px;" role="img" aria-label="Gemeindename in syrischer Schrift"></span>
    <span class="name" style="left:99px; top:43px;">Syrisch-Orthodoxe Gemeinde St. Ephräm in Graz</span>
  </div>
  <div class="quote on-photo" style="left:97px; top:98px;">
    <span class="line first">„Ich aber sage dir:</span>
    <span class="line">Du bist Petrus, und auf diesen Felsen werde</span>
    <span class="line">ich meine Kirche bauen, und die Mächte der</span>
    <span class="line">Unterwelt werden sie nicht überwältigen.“</span>
  </div>
  <div class="reference on-photo" style="right:99px; top:172px;">Matthaeus 16:18</div>
</div>

<!-- Variante 7 -->
<span class="variant-number" style="left:594px; top:648px;">7</span>
<div class="flyer" style="left:624px; top:661px;">
  <div class="hatch-band" style="left:0; top:21px; width:456px; height:7px;"></div>
  <div class="hatch-band" style="left:115px; top:177px; width:341px; height:6px;"></div>
  <div class="madonna-art faint" style="left:0; top:50px; width:118px; height:171px;" role="img" aria-label="Zeichnung: Ikone der Gottesmutter mit Kind, hellgrau"></div>
  <div class="quote" style="left:140px; top:59px;">
    <span class="line first">„Ich aber sage dir:</span>
    <span class="line">Du bist Petrus, und auf diesen Felsen werde</span>
    <span class="line">ich meine Kirche bauen, und die Mächte der</span>
    <span class="line">Unterwelt werden sie nicht überwältigen.“</span>
  </div>
  <div class="reference" style="right:44px; top:133px;">Matthaeus 16:18</div>
</div>

<!-- Variante 8 -->
<span class="variant-number" style="left:594px; top:922px;">8</span>
<div class="flyer" style="left:624px; top:935px;">
  <svg class="shape" width="456" height="221" viewBox="0 0 456 221" aria-hidden="true">
    <polygon points="0,0 456,0 456,160 145,190 52,118 0,64" fill="var(--gold)"/>
    <polygon points="0,64 52,118 46,124 0,82" fill="var(--gold-light)"/>
    <polygon points="145,190 456,160 456,170 145,197" fill="var(--gold-light)"/>
    <polygon points="145,197 456,170 456,178 145,202" fill="var(--beige)"/>
  </svg>
  <div class="madonna-art" style="left:27px; top:43px; width:118px; height:153px;" role="img" aria-label="Zeichnung: Ikone der Gottesmutter mit Kind"></div>
  <div class="quote on-gold" style="left:154px; top:55px;">
    <span class="line first">„Ich aber sage dir:</span>
    <span class="line">Du bist Petrus, und auf diesen Felsen werde</span>
    <span class="line">ich meine Kirche bauen, und die Mächte der</span>
    <span class="line">Unterwelt werden sie nicht überwältigen.“</span>
  </div>
  <div class="reference on-gold" style="right:28px; top:130px;">Matthaeus 16:18</div>
</div>

</body>
</html>
```